business card design for a small scale specialty cut flower farm

We need a business card design for Hollowmere Bloom Farm based in Langley, BC, Canada. We produce specialty, high-end cut flowers and sell locally to florists, local shops and markets and the end user through bouquet subscriptions. The final business card design should be memorable and have a timeless or vintage feel. We would prefer a square shape.
Updates

Target Market(s)

florists, shops and seasonal markets, local flower lovers

Industry/Entity Type

Floral

Contact Information for Business Card

Tamsin Ellery Voss, Grower
Langley, BC, Canada
website: hollowmerebloomfarm.example
instagram: @hollowmerebloomfarm
Tel: 555.317.4290
facebook: www.facebook.example/hollowmereblooms/

Font styles to use
Serif
Decorative
Script

Requirements
Must have
• soft black background colour on front side, the included logo and catch phrase: Fresh Local Seasonal
Nice to have
• phone number and website address on front of card, included photo 6539 incorporated onto the back, possibly photo 6609 as well.

```html
<!DOCTYPE html>
<html lang="en">
<head>
<meta charset="utf-8">
<title>Hollowmere Bloom Farm — Business Card</title>
<link rel="stylesheet" href="https://fonts.googleapis.com/css2?family=Great+Vibes&family=Lato:wght@400&family=Cinzel:wght@400&family=Cormorant+Garamond:wght@500&family=Kaushan+Script&family=Parisienne&display=swap">
<style>
  :root {
    --stage: #dcdcdc;
    --card-light: #ffffff;
    --card-dark: #231f20;
    --ink: #1d1b1b;
    --ink-soft: #3a3636;
    --paper-text: #ffffff;
    --blush: #eeb3d3;
    --blush-pale: #f4d6e6;
    --leaf: #4a7d4c;
    --leaf-dark: #35603a;
  }
  * { box-sizing: border-box; margin: 0; padding: 0; }
  html, body {
    width: 1200px;
    height: 1200px;
    overflow: hidden;
    background: var(--stage);
  }
  .stage { position: relative; width: 1200px; height: 1200px; }
  .card {
    position: absolute;
    left: 376px;
    width: 448px;
    height: 448px;
    overflow: hidden;
    text-align: center;
  }

  /* Logo side */
  .card--logo { top: 102px; background: var(--card-light); color: var(--ink); }
  .logo-dot {
    position: absolute;
    left: 194px;
    top: 112px;
    width: 60px;
    height: 60px;
    border-radius: 50%;
    background: var(--blush-pale);
  }
  .brand-name {
    position: absolute;
    left: 0; right: 0;
    top: 196px;
    font-family: "Great Vibes", cursive;
    font-weight: 400;
    line-height: 1;
    color: var(--ink);
  }
  .brand-name__main { display: block; font-size: 70px; }
  .brand-name__sub { display: block; font-size: 36px; margin-top: -4px; }
  .tagline {
    position: absolute;
    left: 0; right: 0;
    top: 318px;
    font-family: "Parisienne", cursive;
    font-size: 19px;
    color: var(--ink-soft);
  }
  .established {
    position: absolute;
    left: 0; right: 0;
    top: 352px;
    font-family: "Lato", sans-serif;
    font-size: 11px;
    letter-spacing: 5px;
    color: var(--ink-soft);
  }

  /* Contact side */
  .card--contact { top: 651px; background: var(--card-dark); color: var(--paper-text); }
  .art { position: absolute; }
  .art--bud {
    left: 0; top: 0; width: 111px; height: 92px;
    background: radial-gradient(ellipse at 30% 25%, var(--leaf) 0%, var(--leaf-dark) 55%, var(--card-dark) 100%);
  }
  .art--leaf-top {
    left: 300px; top: 0; width: 148px; height: 100px;
    background: radial-gradient(ellipse at 75% 25%, var(--leaf) 0%, var(--leaf-dark) 60%, var(--card-dark) 100%);
  }
  .art--petal-side {
    left: 0; top: 228px; width: 52px; height: 160px;
    background: linear-gradient(90deg, var(--blush-pale) 0%, var(--blush) 70%, var(--card-dark) 100%);
  }
  .art--petal-low {
    left: 0; top: 388px; width: 150px; height: 60px;
    background: linear-gradient(90deg, var(--blush) 0%, var(--blush) 70%, var(--card-dark) 100%);
  }
  .art--leaf-low {
    left: 373px; top: 395px; width: 75px; height: 53px;
    background: radial-gradient(ellipse at 80% 80%, var(--leaf) 0%, var(--leaf-dark) 55%, var(--card-dark) 100%);
  }
  .motto {
    position: absolute;
    left: 151px; top: 74px;
    width: 143px; height: 163px;
    border: 2px solid var(--paper-text);
    list-style: none;
    font-family: "Cinzel", serif;
    font-size: 22px;
    line-height: 1;
    padding-top: 25px;
  }
  .motto li + li { margin-top: 20px; }
  .owner { position: absolute; left: 0; right: 0; top: 264px; }
  .owner__name { font-family: "Kaushan Script", cursive; font-size: 38px; line-height: 1; }
  .owner__role { font-family: "Cinzel", serif; font-size: 14px; margin-top: 0; }
  .contact {
    position: absolute;
    left: 0; right: 0;
    top: 346px;
    font-family: "Cormorant Garamond", serif;
    font-weight: 500;
  }
  .contact__web { font-size: 16px; letter-spacing: 0.3px; text-transform: uppercase; }
  .contact__phone { font-size: 19px; margin-top: 2px; }
  .contact__social {
    display: flex;
    justify-content: center;
    align-items: center;
    gap: 6px;
    margin-top: 4px;
    font-size: 11px;
  }
  .contact__social-dot { width: 12px; height: 12px; border-radius: 50%; background: var(--paper-text); }
</style>
</head>
<body>
<main class="stage">

  <section class="card card--logo" aria-label="Business card, logo side">
    <span class="logo-dot" aria-hidden="true"></span>
    <h1 class="brand-name">
      <span class="brand-name__main">Hollowmere</span>
      <span class="brand-name__sub">Bloom Farm</span>
    </h1>
    <p class="tagline">Specialty Cut Flowers</p>
    <p class="established">EST.2019</p>
  </section>

  <section class="card card--contact" aria-label="Business card, contact side">
    <div class="art art--bud" role="img" aria-label="Watercolour illustration of a rose bud with green sepals"></div>
    <div class="art art--leaf-top" role="img" aria-label="Watercolour illustration of a large serrated green leaf"></div>
    <div class="art art--petal-side" role="img" aria-label="Watercolour illustration of a pink rose petal"></div>
    <div class="art art--petal-low" role="img" aria-label="Watercolour illustration of a pink rose petal"></div>
    <div class="art art--leaf-low" role="img" aria-label="Watercolour illustration of a green leaf tip"></div>

    <ul class="motto">
      <li>Fresh</li>
      <li>Local</li>
      <li>Seasonal</li>
    </ul>

    <div class="owner">
      <p class="owner__name">Tamsin Ellery Voss</p>
      <p class="owner__role">Owner</p>
    </div>

    <div class="contact">
      <p class="contact__web">hollowmerebloomfarm.example</p>
      <p class="contact__phone">(555) 317-4290</p>
      <p class="contact__social"><span class="contact__social-dot" aria-hidden="true"></span>@hollowmerebloomfarm</p>
    </div>
  </section>

</main>
</body>
</html>
```